Global (re)insurance broker needs a business card design

We need a classic business card for our company that is headquartered in SG, with offices in Malaysia and Dubai. We specialise in insurance and reinsurance broking and consultancy for our global clients.

```html
<!DOCTYPE html>
<html lang="en">
<head>
<meta charset="utf-8">
<title>Business Card – Front and Back</title>
<link rel="stylesheet" href="https://fonts.googleapis.com/css2?family=Montserrat:wght@400;500;600;700&display=swap">
<style>
  :root {
    --stage: #3a3a3a;
    --card-white: #ffffff;
    --brand-blue: #244796;
    --brand-green: #c1dcb4;
    --ink-white: #ffffff;
    --divider: rgba(255,255,255,0.45);
  }
  * { box-sizing: border-box; margin: 0; padding: 0; }
  html, body {
    width: 1200px; height: 1200px; overflow: hidden;
    background: var(--stage);
    font-family: "Montserrat", Arial, sans-serif;
  }
  .stage {
    width: 1200px; height: 1200px;
    display: flex; flex-direction: column; align-items: center; justify-content: center;
    gap: 70px;
  }
  .card {
    position: relative;
    width: 770px; height: 440px;
    border-radius: 36px;
    overflow: hidden;
    box-shadow: 0 18px 40px rgba(0,0,0,0.45);
  }

  /* Front */
  .card-front { background: var(--card-white); }
  .front-top {
    position: absolute; left: 0; top: 0; width: 100%; height: 238px;
    display: flex; align-items: center; justify-content: center;
  }
  .wordmark {
    font-weight: 600;
    letter-spacing: 6px;
    line-height: 1;
  }
  .front-top .wordmark { color: var(--brand-blue); font-size: 78px; }
  .accent-rule {
    position: absolute; left: 0; top: 238px; width: 100%; height: 10px;
    background: var(--brand-green);
  }
  .front-band {
    position: absolute; left: 0; top: 256px; width: 100%; height: 184px;
    background: var(--brand-blue);
    display: flex; align-items: center;
  }
  .identity {
    width: 330px; padding-left: 92px; color: var(--ink-white);
  }
  .identity .full-name { font-weight: 700; font-size: 30px; letter-spacing: 0.5px; }
  .identity .position { font-weight: 400; font-size: 20px; margin-top: 2px; letter-spacing: 1px; }
  .band-divider {
    width: 1px; height: 120px; background: var(--divider); margin: 0 42px 0 28px;
  }
  .contact-list {
    list-style: none; color: var(--ink-white);
    font-size: 17px; line-height: 1.25;
  }
  .contact-list li { display: flex; align-items: flex-start; gap: 10px; margin: 3px 0; }
  .contact-list svg { width: 17px; height: 17px; flex: none; margin-top: 2px; fill: var(--ink-white); }

  /* Back */
  .card-back {
    background: var(--brand-blue);
    display: flex; align-items: center; justify-content: center;
  }
  .card-back .wordmark { color: var(--ink-white); font-size: 96px; }
</style>
</head>
<body>
<main class="stage">

  <section class="card card-front" aria-label="Business card front">
    <div class="front-top">
      <span class="wordmark">MERIDANE</span>
    </div>
    <div class="accent-rule"></div>
    <div class="front-band">
      <div class="identity">
        <p class="full-name">FULL NAME</p>
        <p class="position">POSITION</p>
      </div>
      <div class="band-divider"></div>
      <ul class="contact-list">
        <li>
          <svg viewBox="0 0 24 24" aria-hidden="true"><path d="M6.6 10.8a15.1 15.1 0 0 0 6.6 6.6l2.2-2.2a1 1 0 0 1 1-.25 11.4 11.4 0 0 0 3.6.57 1 1 0 0 1 1 1V20a1 1 0 0 1-1 1A17 17 0 0 1 3 4a1 1 0 0 1 1-1h3.5a1 1 0 0 1 1 1c0 1.25.2 2.45.57 3.57a1 1 0 0 1-.25 1z"/></svg>
          <span>(000) 000 0000</span>
        </li>
        <li>
          <svg viewBox="0 0 24 24" aria-hidden="true"><path d="M2 5h20v14H2z M4 7v.4l8 5.2 8-5.2V7z" fill-rule="evenodd"/></svg>
          <span>email@company.com</span>
        </li>
        <li>
          <svg viewBox="0 0 24 24" aria-hidden="true"><path d="M12 2a10 10 0 1 0 0 20 10 10 0 0 0 0-20zm6.9 6h-3a15 15 0 0 0-1.3-3.9A8 8 0 0 1 18.9 8zM12 4c.8 1.2 1.5 2.5 1.9 4h-3.8c.4-1.5 1.1-2.8 1.9-4zM4.3 14a8 8 0 0 1 0-4h3.4a16 16 0 0 0 0 4zm.8 2h3a15 15 0 0 0 1.3 3.9A8 8 0 0 1 5.1 16zm3-8h-3a8 8 0 0 1 4.3-3.9A15 15 0 0 0 8.1 8zM12 20c-.8-1.2-1.5-2.5-1.9-4h3.8c-.4 1.5-1.1 2.8-1.9 4zm2.3-6H9.7a14 14 0 0 1 0-4h4.6a14 14 0 0 1 0 4zm.3 5.9a15 15 0 0 0 1.3-3.9h3a8 8 0 0 1-4.3 3.9zm1.7-5.9a16 16 0 0 0 0-4h3.4a8 8 0 0 1 0 4z"/></svg>
          <span>www.company.com</span>
        </li>
        <li>
          <svg viewBox="0 0 24 24" aria-hidden="true"><path d="M12 2a7 7 0 0 0-7 7c0 5.2 7 13 7 13s7-7.8 7-13a7 7 0 0 0-7-7zm0 9.5A2.5 2.5 0 1 1 12 6.5a2.5 2.5 0 0 1 0 5z"/></svg>
          <span>123 Name Street, 000<br>Your City, 00000-000</span>
        </li>
      </ul>
    </div>
  </section>

  <section class="card card-back" aria-label="Business card back">
    <span class="wordmark">MERIDANE</span>
  </section>

</main>
</body>
</html>
```